Trade Show Banner
Clean and modern
Need a banner created for a trade show. The banner will be 8 ft x 8ft. I'm trying to convey messages to two different groups. On one side of the banner the message should say: "Start Selling" Record, upload, sell Sell videos, pictures and picsets right from your cell phone On the other side of the banner the message should say: "Start Watching" Watch the most intimate moments from your favorite pornstars, amateurs and cam girls. Somewhere on the banner it should display the following: - our logo - our URL (www.velvareelhub.example) - Zorbify logo with the following URL underneath - Quellan Deck logo with the following URL underneath The banner will be hung at the back of the booth behind the table, so images/text should not go all the way to the bottom of the banner Note, from banner manufacturers website: Mira-Loft Works’s durable indoor/outdoor retail banners are made from a weatherproof 13 oz. vinyl that will not rip or fray when exposed to outside weather conditions like wind or rain. A double-stitched sewn hem can be included to further reduce fraying if the banner is hung at an outdoor venue. The resilient 15 mil. vinyl is printed with waterproof solvent inks so that your message, which is printed by our large format digital printers at 720 DPI resolution, can be seen wherever you choose to display it. Aluminum grommets measuring ¾” in diameter can be added to the banner at no additional cost in order to easily hang the display with rope or hooks. We recommend placing grommets every two feet on a custom retail banner so the vinyl material does not billow when hung. The wrinkle-resistant vinyl banner can be rolled together when not in use for added convenience when traveling with the display or placing it in storage. Leave a 1.5” margin around all sides where no text or images occur when creating the artwork to avoid disruption from the stitch line. We need all files to be in CMYK and to have a resolution of 150 DPI. PDF, JPEG, EPS, AI, PSD and TIFF files are acceptable. All files should be created at 100% of the desired banner size and will be converted to a JPEG before printing.
The text / images should be on the top 3/4 of the banner. The banner will be displayed in the back of the booth and there will be a stand fold out table in front.

```html
<!DOCTYPE html>
<html lang="en">
<head>
<meta charset="utf-8">
<title>Velvareel Hub – Trade Show Banner</title>
<link rel="stylesheet" href="https://fonts.googleapis.com/css2?family=Comfortaa:wght@700&family=Asap:wght@600;700&family=Nunito+Sans:wght@300;700;800&display=swap">
<style>
  :root {
    --bg-light: #fdf0f2;
    --bg-pink: #f9cdd7;
    --brand-pink: #ef5f97;
    --ink: #262224;
    --band-dark: #6e1232;
    --band-mid: #8d1b45;
    --band-bright: #e24f93;
    --badge: #111111;
    --white: #ffffff;
    --skin-a: #e9b48f;
    --skin-b: #d79a74;
  }
  * { margin: 0; padding: 0; box-sizing: border-box; }
  html, body { width: 1200px; height: 1200px; overflow: hidden; }
  body {
    position: relative;
    background:
      radial-gradient(circle at 20% 15%, rgba(255,255,255,0.7) 0, rgba(255,255,255,0) 260px),
      radial-gradient(circle at 85% 30%, rgba(255,255,255,0.55) 0, rgba(255,255,255,0) 220px),
      radial-gradient(circle at 50% 60%, var(--bg-light) 0, var(--bg-pink) 900px);
    font-family: "Nunito Sans", sans-serif;
    color: var(--ink);
  }
  .brand-dot {
    position: absolute; left: 288px; top: 64px;
    width: 62px; height: 62px; border-radius: 50%;
    background: var(--brand-pink);
  }
  .brand-name {
    position: absolute; left: 0; top: 150px; width: 1200px;
    text-align: center;
    font-family: "Comfortaa", sans-serif; font-weight: 700;
    font-size: 118px; letter-spacing: -3px; line-height: 1;
    color: var(--ink);
  }
  .model-photo {
    position: absolute; left: 300px; top: 392px; width: 700px; height: 478px;
  }
  .pitch { position: absolute; top: 305px; width: 420px; }
  .pitch--sell { left: 89px; text-align: left; }
  .pitch--watch { right: 89px; text-align: right; }
  .pitch__title {
    font-family: "Asap", sans-serif; font-weight: 700;
    font-size: 46px; color: var(--brand-pink); line-height: 1.2;
  }
  .pitch__lead { font-weight: 700; font-size: 33px; line-height: 1.3; margin-top: 6px; }
  .pitch__body { font-weight: 300; font-size: 35px; line-height: 1.36; }
  .pitch--watch .pitch__body { margin-top: 6px; }
  .store { position: absolute; top: 610px; width: 222px; text-align: center; }
  .store--left { left: 89px; }
  .store--right { left: 885px; }
  .store__badge {
    display: flex; align-items: center; justify-content: center; gap: 12px;
    height: 64px; border-radius: 8px;
    background: linear-gradient(#3a3a3a, var(--badge) 55%);
    color: var(--white);
    font-family: "Nunito Sans", sans-serif; font-weight: 700; font-size: 28px;
  }
  .store__mark { width: 22px; height: 22px; border-radius: 50%; background: var(--white); }
  .store__info { margin-top: 10px; font-weight: 800; font-size: 16px; line-height: 1.8; }
  .url-band {
    position: absolute; left: 0; top: 836px; width: 1200px; height: 114px;
    background: linear-gradient(90deg, var(--band-dark) 0%, var(--band-mid) 55%, var(--band-bright) 100%);
    border-top: 3px solid rgba(255,255,255,0.35);
    border-bottom: 3px solid rgba(255,255,255,0.35);
    display: flex; align-items: center; justify-content: center;
  }
  .url-band__text {
    font-family: "Comfortaa", sans-serif; font-weight: 700;
    font-size: 58px; color: var(--white); letter-spacing: -1px;
  }
</style>
</head>
<body>
  <div class="brand-dot"></div>
  <div class="brand-name">velvareelhub</div>

  <svg class="model-photo" viewBox="0 0 700 478" role="img" aria-label="Photo of a seated model hugging her knees, facing the viewer">
    <defs>
      <radialGradient id="skinTone" cx="50%" cy="50%" r="50%">
        <stop offset="0" stop-color="var(--skin-a)"/>
        <stop offset="0.7" stop-color="var(--skin-b)" stop-opacity="0.85"/>
        <stop offset="1" stop-color="var(--skin-b)" stop-opacity="0"/>
      </radialGradient>
    </defs>
    <ellipse cx="350" cy="250" rx="340" ry="235" fill="url(#skinTone)"/>
  </svg>

  <section class="pitch pitch--sell">
    <h2 class="pitch__title">Start Selling</h2>
    <p class="pitch__lead">Record, upload, sell</p>
    <p class="pitch__body">Sell videos, pictures<br>and picsets right from<br>your cell phone.</p>
  </section>

  <section class="pitch pitch--watch">
    <h2 class="pitch__title">Start Watching</h2>
    <p class="pitch__body">Watch the most intimate<br>moments from your<br>favorite pornstars,<br>amateurs and cam girls.</p>
  </section>

  <div class="store store--left">
    <div class="store__badge"><span class="store__mark"></span>Zorbify</div>
    <p class="store__info">Search: VRH<br>URL: vrh.example/app</p>
  </div>

  <div class="store store--right">
    <div class="store__badge"><span class="store__mark"></span>Quellan Deck</div>
    <p class="store__info">Search: VRH2<br>URL: vrh.example/app2</p>
  </div>

  <div class="url-band">
    <span class="url-band__text">www.velvareelhub.example</span>
  </div>
</body>
</html>
```